project - Kestra Nook

Dear designers, I'm Looking for an appealing new business card design to represent us for our new e-cigarette store: The KestrA Nook. Knowledgeable and friendly staff we aim for superior customer service with a positive atmosphere. Classic feel with modern touch is what we are aiming for . Lime green font and grey back round is the original color scheme but we are flexible and open to suggestions. I added some doodles to show you where my mind is at. address: 4308 87 Ave NW Edmonton, AB (inside the hollin trade hall)web: thekestranook.com email: info@thekestranook.com phone : 587.555.0148 Thanks and am looking forward to seeing your creative , fresh and innovative designs.
Good luck everybody!
Jonas
lime green and charcoal grey please. thanks
Business
The KestrA Nook

```html
<!DOCTYPE html>
<html lang="en">
<head>
<meta charset="utf-8">
<title>The KestrA Nook – Business Card</title>
<link href="https://fonts.googleapis.com/css2?family=Lato:wght@400;900&display=swap" rel="stylesheet">
<style>
  :root {
    --backdrop: #a0673d;
    --card-charcoal: #1f1f1f;
    --lime: #5cbf3c;
    --ink-light: #f2f2f2;
  }
  * { margin: 0; padding: 0; box-sizing: border-box; }
  html, body {
    width: 1200px;
    height: 800px;
    overflow: hidden;
  }
  body {
    position: relative;
    background: var(--backdrop);
    font-family: "Lato", Arial, sans-serif;
  }
  .card {
    position: absolute;
    left: 258px;
    width: 530px;
    height: 325px;
    background: var(--card-charcoal);
    border-radius: 12px;
  }
  .card--front { top: 86px; }
  .card--back  { top: 427px; }

  .brand-name {
    position: absolute;
    left: 0;
    right: 0;
    text-align: center;
    color: var(--lime);
    font-weight: 900;
    font-size: 46px;
    letter-spacing: 0.5px;
    line-height: 1;
  }
  .card--front .brand-name { top: 136px; }
  .card--back  .brand-name { top: 56px; }

  .contact-list {
    position: absolute;
    top: 148px;
    left: 0;
    right: 0;
    list-style: none;
    display: flex;
    flex-direction: column;
    align-items: center;
    gap: 6px;
  }
  .contact-item {
    display: flex;
    align-items: center;
    gap: 8px;
    color: var(--ink-light);
    font-size: 15px;
    line-height: 18px;
  }
  .contact-icon {
    width: 16px;
    height: 16px;
    fill: var(--lime);
    flex: none;
  }
  .address {
    position: absolute;
    top: 242px;
    left: 0;
    right: 0;
    text-align: center;
    color: var(--ink-light);
    font-size: 15px;
    line-height: 20px;
    font-style: normal;
  }
</style>
</head>
<body>
  <section class="card card--front">
    <h1 class="brand-name">The KestrA Nook</h1>
  </section>

  <section class="card card--back">
    <p class="brand-name">The KestrA Nook</p>

    <ul class="contact-list">
      <li class="contact-item">
        <svg class="contact-icon" viewBox="0 0 16 16" aria-hidden="true">
          <path d="M2 6c0-2 2.5-3 6-3s6 1 6 3v1h-3V5.5H5V7H2z"/>
          <path d="M4 8h8l2 5H2z"/>
          <circle cx="8" cy="10.5" r="1.4" fill="#1f1f1f"/>
        </svg>
        <span>587.555.0148</span>
      </li>
      <li class="contact-item">
        <svg class="contact-icon" viewBox="0 0 16 16" aria-hidden="true">
          <rect x="1" y="3" width="14" height="10" rx="1"/>
          <path d="M1.5 4l6.5 5 6.5-5" fill="none" stroke="#1f1f1f" stroke-width="1.3"/>
        </svg>
        <span>info@thekestranook.com</span>
      </li>
      <li class="contact-item">
        <svg class="contact-icon" viewBox="0 0 16 16" aria-hidden="true">
          <circle cx="8" cy="8" r="7.5"/>
          <rect x="0.5" y="6.3" width="15" height="3.4" fill="#1f1f1f"/>
          <rect x="3" y="7.3" width="10" height="1.4" fill="var(--lime)"/>
        </svg>
        <span>www.thekestranook.com</span>
      </li>
    </ul>

    <address class="address">
      4308 87 Ave NW Edmonton, AB<br>
      (Inside the Hollin Trade Hall)
    </address>
  </section>
</body>
</html>
```